Kelvo Tech Oz Business card revamp

We are looking to revamp our business card design. We are hoping to change our colours to dark navey blue, gray, white and black but are open to keeping the same if a good design is submited. We are after somthing a bit differnt not just boring business card. I have attached a copy of our current card. We Want to keep the same logo design which i have attached a few to hopfully help you in this process. We are after a design that can be personalized to separate 4 people

Colors
0455a3
ffffff
000000
cbcbcb

Requirements
Must have
• Kelvo Tech Logo, address 3/41 Mallory Court, Wexhill 4218, phone number, Name and position

```html
<!DOCTYPE html>
<html lang="en">
<head>
<meta charset="utf-8">
<title>Kelvo Tech Oz – Business Cards</title>
<link rel="stylesheet" href="https://fonts.googleapis.com/css2?family=Ubuntu:wght@400;500;700&display=swap">
<style>
  :root {
    --stage: #d9d9d9;
    --card-black: #0b0b0b;
    --card-white: #ffffff;
    --accent-orange: #f07a22;
    --brand-blue: #1f7fd1;
    --soft-grey: #cbcbcb;
  }
  * { box-sizing: border-box; margin: 0; padding: 0; }
  html, body { width: 1200px; height: 800px; overflow: hidden; }
  body {
    background: var(--stage);
    font-family: "Ubuntu", sans-serif;
    display: flex;
    align-items: center;
    justify-content: center;
    gap: 60px;
  }
  .card {
    width: 525px;
    height: 300px;
    border-radius: 4px;
    position: relative;
    overflow: hidden;
    box-shadow: 0 6px 18px rgba(0,0,0,.25);
  }

  /* Shared brand lockup */
  .brand {
    display: flex;
    align-items: center;
    gap: 12px;
  }
  .brand__dot {
    width: 34px; height: 34px;
    border-radius: 50%;
    background: var(--accent-orange);
    flex: none;
  }
  .brand__name {
    color: var(--brand-blue);
    font-size: 46px;
    font-weight: 700;
    line-height: 1;
  }
  .web {
    color: var(--accent-orange);
    font-weight: 700;
    font-size: 16px;
  }

  /* Back of card */
  .card--back {
    background: var(--card-black);
    display: flex;
    flex-direction: column;
    align-items: center;
    justify-content: center;
    gap: 14px;
  }
  .tagline {
    color: var(--card-white);
    font-size: 14px;
    font-weight: 500;
    letter-spacing: .3px;
  }
  .card--back .web { margin-top: 18px; }

  /* Front of card */
  .card--front { background: var(--card-white); }
  .front__top {
    height: 168px;
    position: relative;
    border-bottom: 3px solid var(--accent-orange);
  }
  .front__top .brand { position: absolute; left: 40px; top: 26px; }
  .front__top .brand__name { font-size: 40px; }
  .front__top .brand__dot { width: 30px; height: 30px; }
  .address {
    position: absolute; left: 82px; top: 78px;
    color: var(--accent-orange);
    font-size: 13px; font-weight: 500;
    line-height: 16px;
  }
  .person-block {
    position: absolute; left: 170px; top: 104px;
  }
  .person-name {
    color: var(--brand-blue);
    font-size: 22px; font-weight: 700;
    line-height: 26px;
  }
  .person-role {
    color: var(--accent-orange);
    font-size: 15px; font-weight: 700;
    line-height: 20px;
    margin-left: 18px;
  }
  .front__top .web {
    position: absolute; right: 30px; top: 132px;
    font-size: 15px;
    line-height: 20px;
  }
  .front__bottom {
    background: var(--card-black);
    height: 132px;
    padding: 20px 30px;
  }
  .phone {
    display: flex; align-items: center; gap: 10px;
    color: var(--brand-blue);
    font-size: 20px; font-weight: 500;
  }
  .phone svg { width: 24px; height: 24px; }
  .services {
    color: var(--accent-orange);
    font-size: 11px;
    line-height: 1.6;
    margin-top: 10px;
    margin-left: 34px;
  }
</style>
</head>
<body>

  <section class="card card--back" aria-label="Card back">
    <p class="tagline">Reliability with dedication to service</p>
    <div class="brand">
      <span class="brand__dot"></span>
      <span class="brand__name">Kelvo Tech</span>
    </div>
    <p class="web">www.kelvotech.com.au</p>
  </section>

  <section class="card card--front" aria-label="Card front">
    <div class="front__top">
      <div class="brand">
        <span class="brand__dot"></span>
        <span class="brand__name">Kelvo Tech</span>
      </div>
      <p class="address">3/41 Mallory Court, Wexhill 4218</p>
      <div class="person-block">
        <p class="person-name">John Doe</p>
        <p class="person-role">Designation</p>
      </div>
      <p class="web">www.kelvotech.com.au</p>
    </div>
    <div class="front__bottom">
      <p class="phone">
        <svg viewBox="0 0 24 24" aria-hidden="true">
          <rect x="2" y="2" width="20" height="20" rx="4" fill="var(--accent-orange)"/>
          <path d="M7 8c0 5 4 9 9 9l1.5-2.5-3-1.5-1 1.2c-1.5-.7-2.9-2.1-3.6-3.6L11 9.5 9.5 6.5z" fill="var(--card-black)"/>
        </svg>
        170-318 (2290)
      </p>
      <p class="services">
        Service Penetrations | Steel Spray Coatings | Intumescent Flames<br>
        Duct Sprays &amp; Wrap | Fire and Smoke Barriers | Fire Rated Walls &amp; Ceilings
      </p>
    </div>
  </section>

</body>
</html>
```